Business Card for New Business

Please design a business card using our logo and font files. This is only one card for one person, as listed in details section.

Industry/Entity Type

Business

Contact Information for Business Card

Carl Voserby

Phone 555.318.6624
Cell 555.581.4096
Email carl@moltravex.com

www.moltravex.com

Address
18250 Brennick Lane #314
Larkhaven, ST 00715

Font styles to use
Sans Serif

Requirements
Must have
• Information listed in detail section. Must be standard card size.

```html
<!DOCTYPE html>
<html lang="en">
<head>
<meta charset="utf-8">
<title>Moltravex – Business Card</title>
<link rel="stylesheet" href="https://fonts.googleapis.com/css2?family=Quicksand:wght@400;500;700&display=swap">
<style>
  :root {
    --bg: #e9e6e2;
    --white: #ffffff;
    --orange: #d2572a;
    --red: #c4262b;
    --charcoal: #262626;
    --ink: #4a4a4a;
    --cream: #f6e6dc;
    --logo-light: #d9d9d9;
  }
  * { margin: 0; padding: 0; box-sizing: border-box; }
  html, body {
    width: 1200px; height: 1200px; overflow: hidden;
    background: var(--bg);
    font-family: "Quicksand", sans-serif;
  }
  .canvas { position: relative; width: 1200px; height: 1200px; }

  .card {
    position: absolute; left: 230px; width: 740px; height: 460px;
    overflow: hidden;
    box-shadow: 0 8px 22px rgba(0,0,0,0.18);
  }
  .card--front { top: 100px; background: var(--orange); }
  .card--back { top: 640px; background: var(--charcoal); }

  /* Front – brand panel */
  .brand-panel {
    position: absolute; left: 0; top: 0; width: 346px; height: 100%;
    background: var(--white);
    border-right: 5px solid var(--red);
  }
  .brand-mark {
    position: absolute; left: 30px; top: 205px;
    display: flex; align-items: center; gap: 12px;
  }
  .brand-mark__dot {
    width: 24px; height: 24px; border-radius: 50%; background: var(--red);
  }
  .brand-mark__name {
    font-size: 46px; font-weight: 500; color: var(--ink); letter-spacing: 1px;
  }
  .web-rule {
    position: absolute; left: 0; right: 0; top: 418px;
    display: flex; align-items: center;
  }
  .web-rule__line { height: 3px; background: var(--red); }
  .web-rule__line--short { width: 34px; }
  .web-rule__line--long { flex: 1; }
  .web-rule__text {
    padding: 0 8px; font-size: 21px; font-weight: 700; color: var(--red);
  }

  /* Front – details */
  .holder-name {
    position: absolute; left: 346px; right: 0; top: 58px;
    text-align: center; font-size: 33px; font-weight: 700; color: var(--white);
  }
  .contact-list { position: absolute; left: 375px; top: 160px; list-style: none; }
  .contact-list li {
    display: flex; align-items: center; height: 38px;
    font-size: 20px; color: var(--cream);
  }
  .contact-icon { width: 28px; height: 28px; margin-right: 38px; flex: none; }
  .address {
    position: absolute; left: 375px; top: 370px;
    display: flex; align-items: flex-start;
  }
  .address .contact-icon { margin-right: 10px; margin-top: 2px; }
  .address__lines { font-size: 23px; line-height: 29px; color: var(--cream); }

  /* Back */
  .back-band-top {
    position: absolute; left: 0; right: 0; top: 0; height: 25px; background: var(--orange);
  }
  .back-band-bottom {
    position: absolute; left: 0; right: 0; bottom: 8px; height: 43px;
    background: var(--orange);
    display: flex; align-items: center; justify-content: center;
    font-size: 21px; font-weight: 700; color: var(--white);
  }
  .back-mark {
    position: absolute; left: 0; right: 0; top: 178px;
    display: flex; align-items: center; justify-content: center; gap: 18px;
  }
  .back-mark__dot { width: 34px; height: 34px; border-radius: 50%; background: var(--red); }
  .back-mark__name {
    font-size: 76px; font-weight: 500; color: var(--logo-light); letter-spacing: 3px;
  }
</style>
</head>
<body>
<main class="canvas">

  <section class="card card--front">
    <div class="brand-panel">
      <div class="brand-mark">
        <span class="brand-mark__dot"></span>
        <span class="brand-mark__name">Moltravex</span>
      </div>
      <div class="web-rule">
        <span class="web-rule__line web-rule__line--short"></span>
        <span class="web-rule__text">www.moltravex.com</span>
        <span class="web-rule__line web-rule__line--long"></span>
      </div>
    </div>

    <h1 class="holder-name">Carl Voserby</h1>

    <ul class="contact-list">
      <li>
        <svg class="contact-icon" viewBox="0 0 28 28" aria-hidden="true">
          <circle cx="14" cy="14" r="13" fill="var(--red)"/>
          <path d="M9.5 7.5l3 3-1.6 1.8c.9 1.9 2.3 3.3 4.2 4.2l1.8-1.6 3 3-1.8 2c-5.2-.4-10.2-5.4-10.6-10.6z" fill="#fff"/>
        </svg>
        Phone 555.318.6624
      </li>
      <li>
        <svg class="contact-icon" viewBox="0 0 28 28" aria-hidden="true">
          <rect x="8" y="3" width="12" height="22" rx="2" fill="#fff"/>
          <rect x="10" y="6" width="8" height="14" fill="var(--red)"/>
        </svg>
        Cell 555.581.4096
      </li>
      <li>
        <svg class="contact-icon" viewBox="0 0 28 28" aria-hidden="true">
          <rect x="4" y="8" width="20" height="14" rx="1" fill="#fff"/>
          <path d="M4 9l10 7 10-7" fill="none" stroke="var(--red)" stroke-width="1.8"/>
          <path d="M10 8l4-4 4 4" fill="none" stroke="#fff" stroke-width="1.8"/>
        </svg>
        Email carl@moltravex.com
      </li>
    </ul>

    <div class="address">
      <svg class="contact-icon" viewBox="0 0 28 28" aria-hidden="true">
        <circle cx="14" cy="14" r="13" fill="var(--red)"/>
        <path d="M14 6a5 5 0 0 0-5 5c0 4 5 10 5 10s5-6 5-10a5 5 0 0 0-5-5z" fill="#fff"/>
        <circle cx="14" cy="11" r="1.8" fill="var(--red)"/>
      </svg>
      <p class="address__lines">18250 Brennick Lane #314<br>Larkhaven, ST 00715</p>
    </div>
  </section>

  <section class="card card--back">
    <div class="back-band-top"></div>
    <div class="back-mark">
      <span class="back-mark__dot"></span>
      <span class="back-mark__name">Moltravex</span>
    </div>
    <div class="back-band-bottom">www.moltravex.com</div>
  </section>

</main>
</body>
</html>
```